Design for a real estate wev portal

Contents and features of the site
---------------------------------
Website in 5 languages: French, Dutch, English, German, Spanish.
English name of the site: Lantern Nest Place
Main purpose of the site:
- allow people to rent their house/ appartment for flatsharing purposes.
- help people wanting to find a room in flatsharing
- help people to find additional roommates for their flatsharing
Key interaction sequence:
1. I create a "group" of people who have common interest/hobbies
2. People who have the same interests/hobbies join my group
3. I look for a house/appartment to host my group
Website structure will be the following:
- Home
- Groups
-- Look for a group
--- Join a group
-- Create a group
- Properties
-- Look for a house/appartement
-- Apply
- Sales conditions
- Contact
- My account
-- My profile
-- My groups OR my properties
Your mission
------------
The client has no graphical guidelines, simply a logo (see attached).
We need a (responsive compliant) design for the following pages (we expect PSD's from you. No HTML nor CSS):
1. homepage (see example and wireframe attached)
2. properties search result list (see wireframe attached)
3. "detailed" form for properties
4. groups search result list
5. "detailed" form for groups
6. my account page
FOR THE COMPETITION step we only expect from you the design of first 2 screens.
Based on that, we will select the designer who will win the project, and will have to design the 4 remaining screens.
Target Market(s)
B2C
Industry/Entity Type
Real Estate
Number of Pages Required
5+ page
Look and feel
Each slider illustrates characteristics of the customer's brand and the style your logo design should communicate.

```html
<!DOCTYPE html>
<html lang="en">
<head>
<meta charset="utf-8">
<title>Lantern Nest Place</title>
<link href="https://fonts.googleapis.com/css2?family=Jost:wght@400;500&family=Open+Sans:wght@400;600&display=swap" rel="stylesheet">
<style>
:root{
  --teal:#1a9cb0;
  --teal-dark:#137f93;
  --green:#6cbf3f;
  --ink:#222;
  --body:#666;
  --grey-band:#eeeeee;
  --tab-dark:#e2e2e2;
  --tab-light:#f2f2f2;
  --white:#fff;
  --line:#dcdcdc;
}
*{box-sizing:border-box;margin:0;padding:0}
html,body{width:1200px;height:2748px;overflow:hidden}
body{position:relative;background:var(--white);font-family:"Open Sans",Arial,sans-serif;color:var(--ink)}
h1,h2{font-weight:400}
.abs{position:absolute}

/* header */
.top-rule{left:0;top:0;width:1200px;height:6px;background:var(--teal)}
.nav-link{top:59px;height:30px;line-height:30px;font-size:16px;letter-spacing:.5px;color:#333}
.nav-home{left:88px;width:91px;border:1.5px solid var(--green);border-radius:16px;text-align:center;color:var(--green)}
.brand{left:490px;top:44px;width:240px;height:44px;display:flex;align-items:center;justify-content:center;gap:10px}
.brand-dot{flex:none;width:18px;height:18px;border-radius:50%;background:var(--green)}
.brand-name{font-family:"Jost",sans-serif;font-weight:500;font-size:25px;color:#333;white-space:nowrap}
.account{left:800px;top:54px;font-size:16px;color:#444}
.lang{left:905px;top:49px;width:100px;height:36px;border:1.5px solid #888;border-radius:18px;font-size:14px;line-height:33px;text-align:center;color:#333}
.login{left:1013px;top:50px;width:99px;height:34px;border-radius:17px;background:var(--green);color:#fff;font-size:15px;line-height:34px;text-align:center}

/* hero */
.hero{left:0;top:123px;width:1200px;height:485px;background:linear-gradient(180deg,#6d7d8f 0%,#7a5a4c 45%,#4f6b3b 80%,#3f5d2c 100%)}
.hero-title{left:0;top:330px;width:1200px;text-align:center;color:#fff;font-size:54px;font-family:"Jost",sans-serif;font-weight:500;letter-spacing:1px;line-height:64px}
.hero-sub{left:0;top:393px;width:1200px;text-align:center;color:#fff;font-size:25px}
.hero-arrow{top:548px;width:28px;height:28px;border-radius:50%;background:rgba(0,0,0,.55)}

/* choose */
.section-title{font-family:"Jost",sans-serif;font-weight:400;font-size:24px;color:var(--teal);letter-spacing:.5px;line-height:30px}
.choice{top:696px;width:238px;height:226px;border:1px solid var(--line);background:#fff}
.choice-img{width:100%;height:172px}
.choice-cap{height:52px;line-height:52px;text-align:center;font-size:14px;color:#444;white-space:nowrap;overflow:hidden}

/* spotlight */
.spot-band{left:0;top:986px;width:1200px;height:461px;background:var(--grey-band)}
.spot-card{width:492px;height:141px;background:#fff;border:1px solid #ddd;display:flex}
.spot-img{width:180px;height:100%;flex:none}
.spot-text{border-left:4px solid var(--green);padding:16px 20px 0 20px;flex:1}
.spot-name{font-size:16px;color:#333;margin-bottom:6px}
.spot-desc{font-size:12.5px;line-height:18px;color:#777;text-align:justify;height:36px;overflow:hidden}
.spot-meta{font-size:13px;line-height:20px;color:var(--teal);margin-top:4px}
.see-more{font-size:13px;color:var(--green)}

/* selling points */
.points-title{font-family:"Jost",sans-serif;font-weight:500;font-size:23px;color:#222;letter-spacing:.5px;line-height:30px}
.points-body{width:458px;font-size:12px;line-height:22.6px;color:#777;text-align:justify}
.read-more{width:112px;height:38px;border:1.5px solid var(--green);border-radius:19px;font-size:13px;color:var(--green);line-height:35px;text-align:center}

/* faq */
.faq-band{left:0;top:1828px;width:1200px;height:550px;background:linear-gradient(135deg,#22a7b8 0%,#1595a8 50%,#1aa3a2 100%)}
.faq-title{left:0;top:1868px;width:1200px;text-align:center;color:#fff;font-family:"Jost",sans-serif;font-weight:500;font-size:25px;letter-spacing:.5px;line-height:32px}
.faq-item{left:86px;width:1026px;height:119px;background:#fff;border-radius:3px;padding:20px 24px 0 38px;font-size:12.6px;line-height:22px;color:#555}
.faq-num{position:absolute;left:18px;top:20px;color:var(--teal);font-weight:600}
.faq-more{color:var(--teal)}
.all-q{left:900px;top:2315px;width:212px;text-align:right;color:#fff;font-size:15px;letter-spacing:.5px}

/* tabs */
.tab{top:2378px;height:81px;line-height:81px;text-align:center;font-size:17px;letter-spacing:.5px;color:#222}
.tab-a{left:0;width:600px;background:var(--tab-dark)}
.tab-b{left:600px;width:600px;background:var(--tab-light)}

/* footer */
.foot-brand{left:95px;top:2560px;display:flex;align-items:center;gap:10px}
.foot-head{top:2514px;font-size:15px;color:#333;letter-spacing:.3px}
.foot-lines{font-size:11.5px;line-height:22px;color:#555;white-space:nowrap}
.mail-input{left:599px;top:2592px;width:148px;height:31px;border:1px solid #ccc;font-size:12px;line-height:29px;padding-left:8px;color:#888}
.mail-submit{left:746px;top:2592px;width:56px;height:31px;background:var(--green);color:#fff;font-size:12px;line-height:31px;text-align:center}
.social{top:2561px;width:24px;height:24px;border-radius:4px;background:#666}
.foot-rule{left:84px;top:2680px;width:1024px;height:1px;background:#ccc}
.copyright{left:0;top:2706px;width:1200px;text-align:center;font-size:12px;color:#333}
</style>
</head>
<body>

<header>
  <div class="abs top-rule"></div>
  <div class="abs nav-link nav-home">HOME</div>
  <div class="abs nav-link" style="left:225px">ABOUT US</div>
  <div class="abs nav-link" style="left:372px">CONTACT</div>
  <div class="abs brand"><span class="brand-dot"></span><span class="brand-name">Lantern Nest Place</span></div>
  <div class="abs account">My Account</div>
  <div class="abs lang">English &#8964;</div>
  <div class="abs login">LOGIN</div>
</header>

<section>
  <div class="abs hero" role="img" aria-label="Large brick family house with a green front lawn"></div>
  <h1 class="abs hero-title">LANTERN NEST PLACE</h1>
  <p class="abs hero-sub">Neque porro quisquam est qui quia dolor sit amet</p>
  <svg class="abs hero-arrow" style="left:1050px" viewBox="0 0 28 28"><path d="M16 8 L10 14 L16 20" stroke="#fff" stroke-width="2.5" fill="none"/></svg>
  <svg class="abs hero-arrow" style="left:1083px" viewBox="0 0 28 28"><path d="M12 8 L18 14 L12 20" stroke="#fff" stroke-width="2.5" fill="none"/></svg>
</section>

<section>
  <h2 class="abs section-title" style="left:92px;top:650px;width:480px;text-align:center">SEARCHING FOR ACCOMMODATION</h2>
  <h2 class="abs section-title" style="left:632px;top:650px;width:480px;text-align:center">I HAVE A HOUSE FOR RENT</h2>
  <div class="abs choice" style="left:92px"><div class="choice-img" role="img" aria-label="Happy family at home" style="background:linear-gradient(135deg,#c9a88e,#e8d4c0 50%,#9cb38a)"></div><div class="choice-cap">I want to rent a room right now !</div></div>
  <div class="abs choice" style="left:334px"><div class="choice-img" role="img" aria-label="Suburban house with a lawn" style="background:linear-gradient(180deg,#b9d3e6,#8fa6b3 50%,#6c9a4e)"></div><div class="choice-cap">I want to join a group</div></div>
  <div class="abs choice" style="left:632px"><div class="choice-img" role="img" aria-label="Bright modern living room interior" style="background:linear-gradient(135deg,#e9e6e2,#b9a89a 55%,#7a4a30)"></div><div class="choice-cap">I want to advertise !</div></div>
  <div class="abs choice" style="left:874px"><div class="choice-img" role="img" aria-label="Villa with a lit pool at dusk" style="background:linear-gradient(180deg,#3b4e7a,#6a6f8d 50%,#3d8fb5)"></div><div class="choice-cap">Why is flatsharing interesting ...</div></div>
</section>

<section>
  <div class="abs spot-band"></div>
  <h2 class="abs section-title" style="left:92px;top:1042px">UNDER THE SPOTLIGHT</h2>
  <h2 class="abs section-title" style="left:621px;top:1042px">UNDER THE SPOTLIGHT</h2>

  <div class="abs spot-card" style="left:92px;top:1088px">
    <div class="spot-img" role="img" aria-label="Group of friends gathered around a laptop" style="background:linear-gradient(135deg,#8a6a52,#c8b19a)"></div>
    <div class="spot-text"><div class="spot-name">A NICE GROUP</div><div class="spot-desc">Ipsum has been the industry's standard dummy text ever since the 1500s, when an unknown printer took a galley.</div><div class="spot-meta">Average age : 35y<br>Men and women welcome</div></div>
  </div>
  <div class="abs spot-card" style="left:92px;top:1244px">
    <div class="spot-img" role="img" aria-label="Young women sitting together on a sofa" style="background:linear-gradient(135deg,#d8d4cc,#a99684)"></div>
    <div class="spot-text"><div class="spot-name">AONTHER NICE GROUP</div><div class="spot-desc">Ipsum has been the industry's standard dummy text ever since the 1500s, when an unknown printer took a galley.</div><div class="spot-meta">Average age : 20 y<br>Only women</div></div>
  </div>
  <div class="abs see-more" style="left:460px;top:1400px">See More Groups &raquo;</div>

  <div class="abs spot-card" style="left:621px;top:1088px">
    <div class="spot-img" role="img" aria-label="Two-storey house with lit windows" style="background:linear-gradient(180deg,#6f8fb8,#9c8a78 60%,#5d7b45)"></div>
    <div class="spot-text"><div class="spot-name">HOUSE Town</div><div class="spot-desc">Ipsum has been the industry's standard dummy text ever since the 1500s, when an unknown printer took a galley.</div><div class="spot-meta">Rent per month<br>Availability</div></div>
  </div>
  <div class="abs spot-card" style="left:621px;top:1244px">
    <div class="spot-img" role="img" aria-label="White house with a green garden" style="background:linear-gradient(180deg,#cfe0ef,#e7e4de 50%,#5f8c3e)"></div>
    <div class="spot-text"><div class="spot-name">APPARTMENT Town</div><div class="spot-desc">Ipsum has been the industry's standard dummy text ever since the 1500s, when an unknown printer took a galley.</div><div class="spot-meta">Rent per month<br>Availability</div></div>
  </div>
  <div class="abs see-more" style="left:996px;top:1400px">See More Home &raquo;</div>
</section>

<section>
  <h2 class="abs points-title" style="left:90px;top:1510px">KEY SELLING POINTS FOR THE ROOMMATES</h2>
  <p class="abs points-body" style="left:90px;top:1551px">Lorem Ipsum has been the industry's standard dummy text ever since the 1500s, when an unknown printer took a galley of type and scrambled it to make a type specimen book. It has survived not only five centuries, but also the leap into electronic typesetting, remaining essentially unchanged. It was popularised in the 1960s with the release of Lettrafold sheets containing Lorem Ipsum passages, and more recently with desktop publishing software like Quillon PageSmith including versions of Lorem Ipsum</p>
  <div class="abs read-more" style="left:88px;top:1724px">Read More &raquo;</div>

  <h2 class="abs points-title" style="left:655px;top:1512px">KEY SELLING POINTS FOR THE OWNERS</h2>
  <p class="abs points-body" style="left:655px;top:1553px">Lorem Ipsum has been the industry's standard dummy text ever since the 1500s, when an unknown printer took a galley of type and scrambled it to make a type specimen book. It has survived not only five centuries, but also the leap into electronic typesetting, remaining essentially unchanged. It was popularised in the 1960s with the release of Lettrafold sheets containing Lorem Ipsum passages, and more recently with desktop publishing software like Quillon PageSmith including versions of Lorem Ipsum</p>
  <div class="abs read-more" style="left:653px;top:1727px">Read More &raquo;</div>
</section>

<section>
  <div class="abs faq-band"></div>
  <h2 class="abs faq-title">EVERYTHING YOU NEED TO KNOW ABOUT FLATSHARING</h2>
  <div class="abs faq-item" style="top:1927px"><span class="faq-num">1.</span>Lorem Ipsum has been the industry's standard dummy text ever since the 1500s, when an unknown printer took a galley of type and scrambled it to make a type specimen book. It has survived not only five centuries, but also the leap into electronic typesetting, remaining essentially unchanged Lorem Ipsum has been the industry's standard dummy text ever since the 1500s, when an unknown printer took a galley of type and scrambled book. &nbsp; <span class="faq-more">Read More &raquo;</span></div>
  <div class="abs faq-item" style="top:2053px"><span class="faq-num">2.</span>Lorem Ipsum has been the industry's standard dummy text ever since the 1500s, when an unknown printer took a galley of type and scrambled it to make a type specimen book. It has survived not only five centuries, but also the leap into electronic typesetting, remaining essentially unchanged Lorem Ipsum has been the industry's standard dummy text ever since the 1500s, when an unknown printer took a galley of type and scrambled book. &nbsp; <span class="faq-more">Read More &raquo;</span></div>
  <div class="abs faq-item" style="top:2180px"><span class="faq-num">3.</span>Lorem Ipsum has been the industry's standard dummy text ever since the 1500s, when an unknown printer took a galley of type and scrambled it to make a type specimen book. It has survived not only five centuries, but also the leap into electronic typesetting, remaining essentially unchanged Lorem Ipsum has been the industry's standard dummy text ever since the 1500s, when an unknown printer took a galley of type and scrambled book. &nbsp; <span class="faq-more">Read More &raquo;</span></div>
  <div class="abs all-q">ALL QUESTIONS &raquo;</div>
</section>

<nav>
  <div class="abs tab tab-a">PRE DEFINES SEARCHES</div>
  <div class="abs tab tab-b">TOOLS AND INFORMATION</div>
</nav>

<footer>
  <div class="abs foot-brand"><span class="brand-dot"></span><span class="brand-name" style="font-size:23px">Lantern Nest Place</span></div>

  <div class="abs foot-head" style="left:333px">CONTACT US</div>
  <div class="abs foot-lines" style="left:333px;top:2549px">Address : 12 Orchard Lane, Millbrook<br>Westvale, MB4 7QR<br>Phone : 555-018-2736.<br>Email : hello@lanternnest.example</div>

  <div class="abs foot-head" style="left:599px">JOIN OUR MAILING LIST</div>
  <div class="abs foot-lines" style="left:599px;top:2544px;width:200px;line-height:16px;font-size:11px;white-space:normal">Your about us information would fit here nicely.</div>
  <div class="abs mail-input">Email address</div>
  <div class="abs mail-submit">Submit</div>

  <div class="abs foot-head" style="left:932px">FOLLOW US OUT THERE</div>
  <div class="abs social" style="left:932px"></div>
  <div class="abs social" style="left:971px"></div>
  <div class="abs social" style="left:1010px"></div>
  <div class="abs social" style="left:1048px"></div>

  <div class="abs foot-rule"></div>
  <div class="abs copyright">Copyright &copy; 2016. All Rights Reserved</div>
</footer>

</body>
</html>
```